Current state of Man's Soul Christian view

I would like an improvement of my design or a reimagining of my design to help people visualize what happens to the soul after we die. The second picture "screenshot 2023" is not my design but gives another idea.

For further information, there are 4 "time" frames that could be sectioned off. Eden is one time. Then adam rebellion and pre messiah earth (with hades/ Sheol). The third time frame is Jesus death, resurrection with the current state of earth. The 4th time frame is the "heavenly realm" which is across all 3 times and is unchanged.

For color ideas, please see my website www.lanternpathnotes.org which has my color theme. But the death of Jesus I would like in some type of red as well as the death of believers.

My goal is something simple, engaging, and easy to understand. If you have any questions please lmk.
Thank you for considering my project.

```html
<!DOCTYPE html>
<html lang="en">
<head>
<meta charset="utf-8">
<title>Current State of Man's Soul</title>
<link rel="stylesheet" href="https://fonts.googleapis.com/css2?family=Bebas+Neue&family=Inter:wght@500;600;700&display=swap">
<style>
  :root{
    --navy:#053a5e;
    --navy-deep:#042f4c;
    --red:#ed1c24;
    --gold:#f2a91c;
    --white:#ffffff;
    --ink:#1d1d1d;
    --panel:rgba(72,72,72,0.78);
    --line:#c9c9c9;
  }
  html,body{margin:0;padding:0;overflow:hidden;}
  body{width:1200px;height:849px;background:#cfd8df;font-family:"Inter",Arial,sans-serif;}
  .canvas{position:relative;width:1200px;height:849px;overflow:hidden;}
  .backdrop{position:absolute;inset:0;
    background:linear-gradient(180deg,#b9cfe2 0%,#e6e1d6 22%,#d9b98f 36%,#6f8b95 44%,#2f5f6a 52%,#7a7f7c 64%,#b9a58f 82%,#cfc1ae 100%);}
  .abs{position:absolute;box-sizing:border-box;}

  .title-bar{left:21px;top:17px;width:888px;height:82px;background:var(--navy);border-radius:12px;}
  .title-bar h1{margin:0;position:absolute;left:22px;top:10px;font-family:"Bebas Neue",Impact,sans-serif;font-weight:400;font-size:64px;line-height:64px;color:#eaf7ff;letter-spacing:1px;}
  .title-bar .divider{position:absolute;left:672px;top:0;width:1px;height:82px;background:#8aa3b5;}
  .brand{position:absolute;left:712px;top:28px;display:flex;align-items:center;gap:10px;color:var(--white);font-size:20px;font-weight:600;}
  .brand .dot{width:14px;height:14px;border-radius:50%;background:var(--white);}

  .heaven-band{left:21px;top:117px;width:1152px;height:93px;border:2px solid #47616f;border-radius:8px;
    background:linear-gradient(90deg,rgba(255,255,255,.55),rgba(220,232,240,.45));}
  .heaven-band h2{margin:0;position:absolute;left:0;width:1200px;top:10px;text-align:center;transform:translateX(-21px);font-size:34px;font-weight:700;color:var(--ink);letter-spacing:-.5px;}
  .hidden-box{left:1019px;top:125px;width:149px;height:77px;background:var(--navy);border-radius:12px;color:var(--white);font-weight:600;font-size:20px;line-height:21px;text-align:center;padding-top:18px;}

  .panel{background:var(--panel);border:2px solid #d6d6d6;border-radius:10px;}
  .panel-left{left:101px;top:230px;width:460px;height:583px;}
  .panel-right{left:750px;top:230px;width:415px;height:585px;}

  .eden{left:24px;top:324px;width:57px;height:128px;border-radius:30px/64px;background:var(--navy);}
  .eden span{position:absolute;left:50%;top:50%;transform:translate(-50%,-50%) rotate(-90deg);color:var(--white);font-size:24px;font-weight:600;white-space:nowrap;}

  .vertical-label{position:absolute;transform:rotate(-90deg);transform-origin:left top;color:var(--white);font-size:21px;font-weight:600;white-space:nowrap;}

  .globe{border-radius:50%;border:1px solid #ddd;}
  .globe-fallen{left:237px;top:255px;width:210px;height:210px;background:radial-gradient(circle at 55% 45%,#2c6a7a 0%,#3b3a30 45%,#c2541a 70%,#1e1c19 100%);}
  .globe-current{left:855px;top:297px;width:176px;height:176px;background:radial-gradient(circle at 45% 40%,#dfe9f3 0%,#3a78b8 35%,#2f6d3c 60%,#0d2e66 100%);}

  .hades{width:176px;height:176px;border-radius:50%;overflow:hidden;border:2px solid #eee;display:flex;}
  .hades .torment{flex:1;background:linear-gradient(180deg,#8a1a12,#e0471b 60%,#5e0f0a);}
  .hades .paradise{flex:1;background:linear-gradient(180deg,#f6d27a,#d9952c 55%,#8a5a1e);border-left:3px solid #fff;}
  .hades-left{left:253px;top:594px;}
  .hades-right{left:855px;top:594px;}
  .realm-label{position:absolute;font-size:15px;font-weight:600;color:var(--white);}
  .realm-label.dark{color:#2a1a08;}

  .name-tag{background:var(--white);border:2px solid #222;border-radius:7px;color:var(--ink);font-weight:700;font-size:19px;text-align:center;line-height:28px;}
  .tag-premessiah{left:221px;top:481px;width:243px;height:32px;}
  .tag-current{left:846px;top:481px;width:198px;height:32px;}

  .death-tag{background:var(--red);color:var(--white);font-weight:700;font-size:22px;line-height:26px;padding-left:10px;}
  .death-left{left:146px;top:522px;width:98px;height:26px;}
  .death-right{left:1023px;top:522px;width:98px;height:26px;}

  .gate-label{position:absolute;color:var(--white);font-size:17px;font-weight:500;line-height:16px;}
  .sheol-label{position:absolute;color:var(--white);font-size:17px;font-weight:500;width:176px;text-align:center;}

  .resurrection{left:589px;top:328px;width:132px;height:54px;background:var(--white);border:2px solid #111;border-radius:8px;color:var(--navy);font-weight:700;font-size:18px;line-height:20px;text-align:center;padding-top:6px;}
  .spirit-box{left:878px;top:231px;width:133px;height:65px;border-radius:5px;background:radial-gradient(circle,#e8eef3 0%,#8fa8bb 70%,#4f6e86 100%);color:var(--ink);font-weight:700;font-size:19px;line-height:20px;text-align:center;padding-top:12px;}
  .sealed{left:1016px;top:271px;color:var(--white);font-size:15px;font-weight:600;}
  .not-sealed{left:873px;top:548px;color:var(--white);font-size:15px;font-weight:700;}
  .jesus-death{left:486px;top:651px;color:var(--white);font-size:20px;font-weight:600;line-height:21px;text-align:center;}
  .cross-mark{left:500px;top:450px;width:46px;height:72px;}
  svg.wires{position:absolute;left:0;top:0;}
</style>
</head>
<body>
<main class="canvas">
  <div class="backdrop" role="img" aria-label="Photo of a sky with clouds over an ocean shoreline and a seagull in flight"></div>

  <header class="abs title-bar">
    <h1>Current State of Man's Soul</h1>
    <div class="divider"></div>
    <div class="brand"><span class="dot"></span>Lanternpath</div>
  </header>

  <section class="abs heaven-band"><h2>3rd Heaven - God’s Heavenly Throne</h2></section>

  <div class="abs panel panel-left"></div>
  <div class="abs panel panel-right"></div>

  <svg class="wires" width="1200" height="849" viewBox="0 0 1200 849" aria-hidden="true">
    <!-- grey guide lines -->
    <g fill="none" stroke="var(--line)" stroke-width="1.5">
      <line x1="445" y1="345" x2="561" y2="345"/>
      <path d="M440 398 H465 a13 13 0 0 1 13 13 V638 a13 13 0 0 1 -13 13 H423"/>
      <line x1="428" y1="703" x2="561" y2="703"/>
      <line x1="285" y1="513" x2="285" y2="615"/><line x1="341" y1="513" x2="341" y2="594"/>
      <line x1="377" y1="513" x2="377" y2="594"/><line x1="407" y1="513" x2="407" y2="615"/>
      <line x1="873" y1="513" x2="873" y2="615"/><line x1="930" y1="513" x2="930" y2="594"/>
      <line x1="968" y1="513" x2="968" y2="594"/><line x1="997" y1="513" x2="997" y2="615"/>
      <line x1="933" y1="210" x2="933" y2="231" stroke="#47616f"/><line x1="955" y1="210" x2="955" y2="231" stroke="#47616f"/>
    </g>
    <!-- red death band -->
    <g fill="var(--red)">
      <path d="M111 230 H136 V547 H1130 V230 H1154 a10 10 0 0 1 10 10 V557 a10 10 0 0 1 -10 10 H111 a10 10 0 0 1 -10 -10 V240 a10 10 0 0 1 10 -10 Z"/>
    </g>
    <!-- navy resurrection path -->
    <g fill="none" stroke="var(--navy-deep)" stroke-width="11" stroke-linejoin="round">
      <path d="M413 732 H644 a10 10 0 0 0 10 -10 V262"/>
      <path d="M943 298 H1138 a9 9 0 0 0 9 -9 V250" stroke-width="7"/>
    </g>
    <g fill="var(--navy-deep)">
      <path d="M654 234 L672 273 L636 273 Z"/>
      <path d="M1147 232 L1159 258 L1135 258 Z"/>
      <path d="M1132 200 L1160 200 L1146 228 Z"/>
    </g>
    <!-- gold chevrons -->
    <g fill="none" stroke="var(--gold)" stroke-width="3.5" stroke-linecap="round" stroke-linejoin="round">
      <path d="M61 385 l7 7 -7 7 M68 385 l7 7 -7 7"/>
      <path d="M472 361 l7 7 -7 7 M479 361 l7 7 -7 7"/>
      <path d="M516 408 l7 7 7 -7 M516 415 l7 7 7 -7"/>
      <path d="M516 589 l7 7 7 -7 M516 596 l7 7 7 -7"/>
      <path d="M473 667 l-7 7 7 7 M466 667 l-7 7 7 7"/>
      <g id="pair">
        <path d="M305 524 l7 7 7 -7 M305 531 l7 7 7 -7"/>
        <path d="M305 574 l7 7 7 -7 M305 581 l7 7 7 -7"/>
      </g>
      <use href="#pair" x="80"/><use href="#pair" x="589"/><use href="#pair" x="670"/>
    </g>
    <path d="M937 215 l7 6 7 -6 M937 221 l7 6 7 -6" fill="none" stroke="var(--navy)" stroke-width="2.5"/>
  </svg>

  <div class="abs eden"><span>Eden</span></div>
  <div class="vertical-label" style="left:106px;top:470px;">Adam Rebellion</div>

  <div class="abs globe globe-fallen" role="img" aria-label="Illustration of a darkened, burning earth globe"></div>
  <div class="abs name-tag tag-premessiah">Pre-Messiah Fallen Earth</div>
  <div class="abs death-tag death-left">DEATH</div>

  <div class="abs cross-mark" role="img" aria-label="Small illustration of Jesus on the cross" style="background:linear-gradient(var(--white),var(--white)) center/4px 100% no-repeat,linear-gradient(var(--white),var(--white)) center 28%/100% 4px no-repeat;"></div>
  <div class="abs jesus-death">JESUS<br>DEATH</div>
  <div class="abs resurrection">Jesus<br>Resurrection</div>

  <div class="gate-label" style="left:192px;top:578px;">Wide Gate</div>
  <div class="gate-label" style="left:415px;top:572px;">Narrow<br>Gate</div>
  <div class="abs hades hades-left" role="img" aria-label="Illustration of Hades split into fiery torment and a golden paradise gateway"><div class="torment"></div><div class="paradise"></div></div>
  <div class="realm-label" style="left:277px;top:623px;">Torment</div>
  <div class="realm-label dark" style="left:348px;top:623px;">Paradise</div>
  <div class="sheol-label" style="left:253px;top:774px;">Hades/Sheol</div>

  <div class="abs hidden-box">Hidden in<br>Christ</div>
  <div class="abs spirit-box">Holy Spirit<br>Descends</div>
  <div class="abs sealed">Sealed in Jesus</div>
  <div class="abs globe globe-current" role="img" aria-label="Photo of planet earth showing the Americas"></div>
  <div class="abs name-tag tag-current">Current Fallen Earth</div>
  <div class="abs death-tag death-right">DEATH</div>
  <div class="abs not-sealed">Not sealed in Jesus</div>

  <div class="gate-label" style="left:776px;top:578px;">Wide Gate</div>
  <div class="gate-label" style="left:1013px;top:578px;">Narrow Gate</div>
  <div class="abs hades hades-right" role="img" aria-label="Illustration of Hades split into fiery torment and a golden paradise gateway"><div class="torment"></div><div class="paradise"></div></div>
  <div class="realm-label" style="left:880px;top:622px;">Torment</div>
  <div class="realm-label dark" style="left:950px;top:622px;">Paradise</div>
  <div class="sheol-label" style="left:855px;top:774px;">Hades/Sheol</div>
</main>
</body>
</html>
```